Construction Route to Market Infographic

We need an infographic for a large wall in our office. We are Drummet Studio and we are a marketing agency for the Construction industry. We want to help show our customers the route to market for their products along with the supply chain. We want to do this in a graphical way that is lively, professional and easy to follow. Drummet Studio brand guidelines should be adhered to. The final design should communicate that we know what we are talking about and you are safe using us a s your marketing agency. We will help you sell your product.

http://www.drummetstudio.co.uk

Target Market(s)

Building Product Manufacturers

Industry/Entity Type

Construction

Font styles to use
Other font styles liked:
• Century Old Style - Regular is the brand font. A complimentary font can also be used.

Requirements
Must have
• Must be in vector format
• Must have company logos where a company is mentioned
• Must be lively and engaging

```html
<!DOCTYPE html>
<html lang="en">
<head>
<meta charset="utf-8">
<title>Construction Route to Market – Drummet Studio</title>
<link href="https://fonts.googleapis.com/css2?family=Archivo+Black&family=Arimo:wght@400;700&family=Varela+Round&display=swap" rel="stylesheet">
<style>
  :root{
    --amber:#fbb216;
    --ink:#4a4a4c;
    --tan:#d5a24a;
    --paper:#ffffff;
    --lemon:#ffe01a;
  }
  html,body{margin:0;padding:0;width:1200px;height:674px;overflow:hidden;background:var(--paper);}
  .mural{display:block;width:1200px;height:674px;}
  .headline{font-family:"Archivo Black",sans-serif;fill:#fff;text-anchor:middle;}
  .section-title{font-family:"Arimo",sans-serif;font-weight:700;font-size:29px;fill:var(--ink);text-anchor:middle;}
  .stage-letter{font-family:"Varela Round",sans-serif;font-size:46px;fill:var(--amber);text-anchor:middle;}
  .badge-text{font-family:"Varela Round",sans-serif;font-size:20px;fill:var(--amber);text-anchor:middle;letter-spacing:1px;}
  .tile-shadow{fill:var(--tan);}
  .tile-face{fill:var(--paper);}
  .tile-dot{fill:var(--ink);}
  .tile-label{font-family:"Arimo",sans-serif;font-size:15.5px;fill:var(--ink);text-anchor:middle;}
  .role-tag{fill:var(--amber);}
  .role-text{font-family:"Arimo",sans-serif;font-size:15px;fill:var(--ink);text-anchor:middle;}
  .flow-amber{fill:none;stroke:var(--amber);stroke-width:9;}
  .flow-ink{fill:none;stroke:var(--ink);stroke-width:8;}
  .arrow{fill:var(--ink);}
  .panel{fill:var(--amber);}
  .backdrop{fill:var(--ink);}
  .pill-frame{fill:var(--amber);}
  .pill-inner{fill:var(--paper);}
  .cta-text{font-family:"Varela Round",sans-serif;font-size:22px;fill:#fff;letter-spacing:1.5px;}
</style>
</head>
<body>
<svg class="mural" viewBox="0 0 2500 1404" xmlns="http://www.w3.org/2000/svg">

  <!-- backdrops -->
  <rect class="backdrop" x="75" y="290" width="1635" height="1114"/>
  <rect class="backdrop" x="1730" y="290" width="670" height="1114"/>

  <!-- header bars -->
  <rect class="backdrop" x="63" y="60" width="552" height="108" rx="28"/>
  <rect class="panel" x="37" y="75" width="605" height="78"/>
  <text class="headline" x="340" y="137" font-size="48">ROUTE TO MARKET</text>
  <rect class="backdrop" x="640" y="107" width="1300" height="14"/>
  <rect class="backdrop" x="738" y="45" width="1107" height="123" rx="30"/>
  <rect class="panel" x="775" y="25" width="1030" height="165" stroke="var(--ink)" stroke-width="8"/>
  <text class="headline" x="1282" y="100" font-size="60">CONSTRUCTION ROUTE</text>
  <text class="headline" x="1290" y="167" font-size="60">TO MARKET</text>
  <rect class="backdrop" x="1932" y="58" width="483" height="108" rx="28"/>
  <rect class="panel" x="1912" y="75" width="523" height="70"/>
  <text class="headline" x="2173" y="131" font-size="48">SUPPLY CHAIN</text>
  <rect class="panel" x="333" y="150" width="14" height="90"/>

  <!-- main flow line -->
  <path class="flow-amber" d="M115 375 V1360 H820 V265 H866"/>
  <path class="flow-amber" d="M930 450 V478 M930 905 V935 M930 1320 V1360 H1815 V1315"/>

  <!-- architect -->
  <rect class="backdrop" x="150" y="258" width="60" height="14"/>
  <circle cx="113" cy="262" r="66" fill="var(--ink)"/>
  <circle cx="113" cy="262" r="56" fill="#d8d8d8" role="img" aria-label="Architect in hard hat illustration"/>
  <rect x="35" y="318" width="150" height="58" rx="26" fill="var(--ink)"/>
  <rect x="41" y="324" width="138" height="46" rx="22" fill="var(--paper)"/>
  <text class="badge-text" x="112" y="355" textLength="122" lengthAdjust="spacingAndGlyphs">ARCHITECT</text>

  <!-- REACH pill -->
  <rect class="pill-frame" x="50" y="530" width="125" height="500" rx="30"/>
  <rect class="pill-inner" x="62" y="542" width="101" height="476" rx="22"/>
  <text class="stage-letter" x="112" y="685">R</text>
  <text class="stage-letter" x="112" y="743">E</text>
  <text class="stage-letter" x="112" y="801">A</text>
  <text class="stage-letter" x="112" y="859">C</text>
  <text class="stage-letter" x="112" y="917">H</text>

  <!-- reach panel -->
  <rect class="panel" x="195" y="235" width="585" height="1087" rx="24"/>
  <g class="section-bar">
    <rect x="210" y="250" width="558" height="40" fill="#fff" stroke="var(--ink)" stroke-width="4"/>
    <text class="section-title" x="489" y="281">REPUTATION</text>
    <rect x="210" y="423" width="558" height="40" fill="#fff" stroke="var(--ink)" stroke-width="4"/>
    <text class="section-title" x="489" y="454">PR</text>
    <rect x="210" y="820" width="558" height="40" fill="#fff" stroke="var(--ink)" stroke-width="4"/>
    <text class="section-title" x="468" y="851">CAMPAIGNS</text>
    <rect x="210" y="1170" width="558" height="40" fill="#fff" stroke="var(--ink)" stroke-width="4"/>
    <text class="section-title" x="489" y="1201">LEAD ACQUISITIONS</text>
  </g>

  <!-- reputation -->
  <g class="tile" transform="translate(210,318)"><rect class="tile-shadow" x="8" y="8" width="128" height="82"/><rect class="tile-face" width="128" height="82"/><circle class="tile-dot" cx="64" cy="2" r="30"/><text class="tile-label" x="64" y="58">Sub-contractor<tspan x="64" dy="18">Influence</tspan></text></g>
  <g class="tile" transform="translate(355,318)"><rect class="tile-shadow" x="8" y="8" width="128" height="82"/><rect class="tile-face" width="128" height="82"/><circle class="tile-dot" cx="64" cy="2" r="30"/><text class="tile-label" x="64" y="58">End User<tspan x="64" dy="18">Influence</tspan></text></g>
  <g class="tile" transform="translate(498,318)"><rect class="tile-shadow" x="8" y="8" width="128" height="82"/><rect class="tile-face" width="128" height="82"/><circle class="tile-dot" cx="64" cy="2" r="30"/><text class="tile-label" x="64" y="58">Colleague / Peer<tspan x="64" dy="18">Influence</tspan></text></g>
  <g class="tile" transform="translate(641,318)"><rect class="tile-shadow" x="8" y="8" width="128" height="82"/><rect class="tile-face" width="128" height="82"/><circle class="tile-dot" cx="64" cy="2" r="30"/><text class="tile-label" x="64" y="58">Previously<tspan x="64" dy="18">Specified</tspan></text></g>

  <!-- PR -->
  <g class="tile" transform="translate(210,492)"><rect class="tile-shadow" x="8" y="8" width="128" height="83"/><rect class="tile-face" width="128" height="83"/><circle class="tile-dot" cx="64" cy="2" r="30"/><text class="tile-label" x="64" y="55">Print<tspan x="64" dy="18">Publications</tspan></text></g>
  <g class="tile" transform="translate(355,492)"><rect class="tile-shadow" x="8" y="8" width="128" height="83"/><rect class="tile-face" width="128" height="83"/><circle class="tile-dot" cx="64" cy="2" r="30"/><text class="tile-label" x="64" y="58">Online<tspan x="64" dy="18">Publications</tspan></text></g>
  <g class="tile" transform="translate(498,492)"><rect class="tile-shadow" x="8" y="8" width="128" height="83"/><rect class="tile-face" width="128" height="83"/><circle class="tile-dot" cx="64" cy="2" r="30"/><text class="tile-label" x="64" y="58">Event<tspan x="64" dy="18">Exhibitions</tspan></text></g>
  <g class="tile" transform="translate(641,492)"><rect class="tile-shadow" x="8" y="8" width="128" height="83"/><rect class="tile-face" width="128" height="83"/><circle class="tile-dot" cx="64" cy="2" r="30"/><text class="tile-label" x="64" y="76">Sponsorship</text></g>

  <g class="tile" transform="translate(210,605)"><rect class="tile-shadow" x="8" y="8" width="128" height="82"/><rect class="tile-face" width="128" height="82"/><circle class="tile-dot" cx="64" cy="2" r="30"/><text class="tile-label" x="64" y="74">Advertising</text></g>
  <g class="tile" transform="translate(355,605)"><rect class="tile-shadow" x="8" y="8" width="128" height="82"/><rect class="tile-face" width="128" height="82"/><circle class="tile-dot" cx="64" cy="2" r="30"/><text class="tile-label" x="64" y="74">TV Shows</text></g>
  <g class="tile" transform="translate(498,605)"><rect class="tile-shadow" x="8" y="8" width="128" height="82"/><rect class="tile-face" width="128" height="82"/><circle class="tile-dot" cx="64" cy="2" r="30"/><text class="tile-label" x="64" y="57">Product Selector<tspan x="64" dy="18">(NPL)</tspan></text></g>
  <g class="tile" transform="translate(641,605)"><rect class="tile-shadow" x="8" y="8" width="128" height="82"/><rect class="tile-face" width="128" height="82"/><circle class="tile-dot" cx="64" cy="2" r="30"/><text class="tile-label" x="64" y="53">Environment<tspan x="64" dy="18">Sensitivity Index</tspan></text></g>

  <g class="tile" transform="translate(210,718)"><rect class="tile-shadow" x="8" y="8" width="128" height="80"/><rect class="tile-face" width="128" height="80"/><circle class="tile-dot" cx="64" cy="2" r="30"/><text class="tile-label" x="64" y="54">Membership<tspan x="64" dy="18">Organizations</tspan></text></g>
  <g class="tile" transform="translate(355,718)"><rect class="tile-shadow" x="8" y="8" width="128" height="80"/><rect class="tile-face" width="128" height="80"/><circle class="tile-dot" cx="64" cy="2" r="30"/><text class="tile-label" x="64" y="72">Directories</text></g>
  <g class="tile" transform="translate(498,718)"><rect class="tile-shadow" x="8" y="8" width="128" height="80"/><rect class="tile-face" width="128" height="80"/><circle class="tile-dot" cx="64" cy="2" r="30"/><text class="tile-label" x="64" y="72">Forums</text></g>
  <g class="tile" transform="translate(641,718)"><rect class="tile-shadow" x="8" y="8" width="128" height="80"/><rect class="tile-face" width="128" height="80"/><circle class="tile-dot" cx="64" cy="2" r="30"/><text class="tile-label" x="64" y="54">Manufacturer’s<tspan x="64" dy="18">Website</tspan></text></g>

  <!-- campaigns -->
  <g class="tile" transform="translate(210,890)"><rect class="tile-shadow" x="8" y="8" width="100" height="65"/><rect class="tile-face" width="100" height="65"/><circle class="tile-dot" cx="50" cy="0" r="25"/><text class="tile-label" x="42" y="61">Paid</text></g>
  <g class="tile" transform="translate(323,890)"><rect class="tile-shadow" x="8" y="8" width="100" height="65"/><rect class="tile-face" width="100" height="65"/><circle class="tile-dot" cx="50" cy="0" r="25"/><text class="tile-label" x="50" y="61">Earned</text></g>
  <g class="tile" transform="translate(436,890)"><rect class="tile-shadow" x="8" y="8" width="100" height="65"/><rect class="tile-face" width="100" height="65"/><circle class="tile-dot" cx="50" cy="0" r="25"/><text class="tile-label" x="50" y="43">Industry<tspan x="50" dy="18">Trends</tspan></text></g>
  <g class="tile" transform="translate(549,890)"><rect class="tile-shadow" x="8" y="8" width="100" height="65"/><rect class="tile-face" width="100" height="65"/><circle class="tile-dot" cx="50" cy="0" r="25"/><text class="tile-label" x="50" y="43">Pay Per<tspan x="50" dy="18">Click</tspan></text></g>

  <g class="tile" transform="translate(210,985)"><rect class="tile-shadow" x="8" y="8" width="100" height="65"/><rect class="tile-face" width="100" height="65"/><circle class="tile-dot" cx="50" cy="0" r="25"/><text class="tile-label" x="50" y="61">Remarketing</text></g>
  <g class="tile" transform="translate(323,985)"><rect class="tile-shadow" x="8" y="8" width="100" height="65"/><rect class="tile-face" width="100" height="65"/><circle class="tile-dot" cx="50" cy="0" r="25"/><text class="tile-label" x="50" y="61">Search</text></g>
  <g class="tile" transform="translate(436,985)"><rect class="tile-shadow" x="8" y="8" width="100" height="65"/><rect class="tile-face" width="100" height="65"/><circle class="tile-dot" cx="50" cy="0" r="25"/><text class="tile-label" x="50" y="61">Email</text></g>
  <g class="tile" transform="translate(549,985)"><rect class="tile-shadow" x="8" y="8" width="100" height="65"/><rect class="tile-face" width="100" height="65"/><circle class="tile-dot" cx="50" cy="0" r="25"/><text class="tile-label" x="50" y="42">Co-brand<tspan x="50" dy="18">Email</tspan></text></g>

  <g class="tile" transform="translate(210,1080)"><rect class="tile-shadow" x="8" y="8" width="100" height="65"/><rect class="tile-face" width="100" height="65"/><circle class="tile-dot" cx="50" cy="0" r="25"/><text class="tile-label" x="50" y="42">Online<tspan x="50" dy="18">Ads / Banners</tspan></text></g>
  <g class="tile" transform="translate(323,1080)"><rect class="tile-shadow" x="8" y="8" width="100" height="65"/><rect class="tile-face" width="100" height="65"/><circle class="tile-dot" cx="50" cy="0" r="25"/><text class="tile-label" x="50" y="42">Landing<tspan x="50" dy="18">Pages</tspan></text></g>
  <g class="tile" transform="translate(436,1080)"><rect class="tile-shadow" x="8" y="8" width="100" height="65"/><rect class="tile-face" width="100" height="65"/><circle class="tile-dot" cx="50" cy="0" r="25"/><text class="tile-label" x="50" y="42">Social<tspan x="50" dy="18">Adverts</tspan></text></g>
  <g class="tile" transform="translate(549,1080)"><rect class="tile-shadow" x="8" y="8" width="100" height="65"/><rect class="tile-face" width="100" height="65"/><circle class="tile-dot" cx="50" cy="0" r="25"/><text class="tile-label" x="50" y="42">Social<tspan x="50" dy="18">Medias</tspan></text></g>

  <g class="tile" transform="translate(662,958)"><rect class="tile-shadow" x="8" y="8" width="100" height="104"/><rect class="tile-face" width="100" height="104"/><circle class="tile-dot" cx="50" cy="0" r="25"/><text class="tile-label" x="50" y="53">Government<tspan x="50" dy="18">Regulation</tspan><tspan x="50" dy="18">Changes</tspan></text></g>

  <!-- lead acquisitions -->
  <g class="tile" transform="translate(210,1238)"><rect class="tile-shadow" x="8" y="8" width="128" height="67"/><rect class="tile-face" width="128" height="67"/><circle class="tile-dot" cx="64" cy="-1" r="26"/><text class="tile-label" x="64" y="44">Grenfold<tspan x="64" dy="18">Leads</tspan></text></g>
  <g class="tile" transform="translate(353,1238)"><rect class="tile-shadow" x="8" y="8" width="128" height="67"/><rect class="tile-face" width="128" height="67"/><circle class="tile-dot" cx="64" cy="-1" r="26"/><text class="tile-label" x="64" y="44">Marlow<tspan x="64" dy="18">BPI</tspan></text></g>
  <g class="tile" transform="translate(496,1238)"><rect class="tile-shadow" x="8" y="8" width="128" height="67"/><rect class="tile-face" width="128" height="67"/><circle class="tile-dot" cx="64" cy="-1" r="26"/><text class="tile-label" x="64" y="44">Keystone<tspan x="64" dy="18">Edge</tspan></text></g>
  <g class="tile" transform="translate(640,1238)"><rect class="tile-shadow" x="8" y="8" width="128" height="67"/><rect class="tile-face" width="128" height="67"/><circle class="tile-dot" cx="64" cy="-1" r="26"/><text class="tile-label" x="64" y="44">Civic Planning<tspan x="64" dy="18">Leads</tspan></text></g>

  <!-- stage pills -->
  <g class="stage">
    <rect class="pill-frame" x="862" y="230" width="123" height="220" rx="28"/>
    <rect class="pill-inner" x="874" y="242" width="99" height="196" rx="20"/>
    <text class="stage-letter" x="923" y="298">A</text>
    <text class="stage-letter" x="923" y="356">C</text>
    <text class="stage-letter" x="923" y="414">T</text>
  </g>
  <g class="stage">
    <rect class="pill-frame" x="862" y="475" width="123" height="430" rx="28"/>
    <rect class="pill-inner" x="874" y="487" width="99" height="406" rx="20"/>
    <text class="stage-letter" x="923" y="533">C</text>
    <text class="stage-letter" x="923" y="591">O</text>
    <text class="stage-letter" x="923" y="649">N</text>
    <text class="stage-letter" x="923" y="707">V</text>
    <text class="stage-letter" x="923" y="765">E</text>
    <text class="stage-letter" x="923" y="823">R</text>
    <text class="stage-letter" x="923" y="881">T</text>
  </g>
  <g class="stage">
    <rect class="pill-frame" x="862" y="930" width="123" height="395" rx="28"/>
    <rect class="pill-inner" x="874" y="942" width="99" height="371" rx="20"/>
    <text class="stage-letter" x="923" y="1001">E</text>
    <text class="stage-letter" x="923" y="1059">N</text>
    <text class="stage-letter" x="923" y="1117">G</text>
    <text class="stage-letter" x="923" y="1175">A</text>
    <text class="stage-letter" x="923" y="1233">G</text>
    <text class="stage-letter" x="923" y="1291">E</text>
  </g>

  <!-- act panel -->
  <rect class="panel" x="1005" y="238" width="680" height="210" rx="24"/>
  <rect class="tile-shadow" x="1070" y="288" width="587" height="150"/>
  <rect class="tile-face" x="1052" y="268" width="587" height="150"/>
  <rect x="1078" y="313" width="278" height="66" rx="33" fill="var(--ink)"/>
  <rect x="1084" y="319" width="266" height="54" rx="27" fill="var(--lemon)"/>
  <text class="cta-text" x="1122" y="355">VISIT WEBSITE &gt;&gt;</text>
  <path d="M1318 365 L1352 380 L1338 386 L1354 406 L1346 412 L1330 392 L1320 402 Z" fill="var(--ink)"/>
  <circle cx="1507" cy="346" r="97" fill="var(--ink)"/>
  <g fill="none" stroke="#fff" stroke-width="6">
    <rect x="1453" y="305" width="110" height="68" rx="4"/>
    <path d="M1507 373 V393 M1490 395 H1524"/>
    <rect x="1484" y="287" width="38" height="48" rx="4" fill="var(--ink)"/>
    <rect x="1514" y="310" width="20" height="32" rx="3" fill="var(--ink)"/>
  </g>

  <!-- convert panel -->
  <rect class="panel" x="1005" y="487" width="680" height="396" rx="24"/>
  <g class="tile" transform="translate(1022,525)"><rect class="tile-shadow" x="8" y="8" width="97" height="82"/><rect class="tile-face" width="97" height="82"/><circle class="tile-dot" cx="48" cy="0" r="31"/><text class="tile-label" x="48" y="56">Sale Call/<tspan x="48" dy="18">Meeting</tspan></text></g>
  <g class="tile" transform="translate(1132,525)"><rect class="tile-shadow" x="8" y="8" width="97" height="82"/><rect class="tile-face" width="97" height="82"/><circle class="tile-dot" cx="48" cy="0" r="31"/><text class="tile-label" x="48" y="58">CPD</text></g>
  <g class="tile" transform="translate(1242,525)"><rect class="tile-shadow" x="8" y="8" width="97" height="82"/><rect class="tile-face" width="97" height="82"/><circle class="tile-dot" cx="48" cy="0" r="31"/><text class="tile-label" x="48" y="58">Factory<tspan x="48" dy="18">Tour</tspan></text></g>
  <g class="tile" transform="translate(1351,525)"><rect class="tile-shadow" x="8" y="8" width="97" height="82"/><rect class="tile-face" width="97" height="82"/><circle class="tile-dot" cx="48" cy="0" r="31"/><text class="tile-label" x="48" y="58">Technical<tspan x="48" dy="18">Call/meeting</tspan></text></g>
  <g class="tile" transform="translate(1460,525)"><rect class="tile-shadow" x="8" y="8" width="97" height="82"/><rect class="tile-face" width="97" height="82"/><circle class="tile-dot" cx="48" cy="0" r="31"/><text class="tile-label" x="48" y="57">Read<tspan x="48" dy="18">Blog</tspan></text></g>
  <g class="tile" transform="translate(1568,525)"><rect class="tile-shadow" x="8" y="8" width="97" height="82"/><rect class="tile-face" width="97" height="82"/><circle class="tile-dot" cx="48" cy="0" r="31"/><text class="tile-label" x="48" y="56">Read<tspan x="48" dy="18">Case Study</tspan></text></g>

  <g class="tile" transform="translate(1022,657)"><rect class="tile-shadow" x="8" y="8" width="97" height="81"/><rect class="tile-face" width="97" height="81"/><circle class="tile-dot" cx="48" cy="0" r="31"/><text class="tile-label" x="48" y="54">BIM<tspan x="48" dy="18">Objects</tspan></text></g>
  <g class="tile" transform="translate(1132,657)"><rect class="tile-shadow" x="8" y="8" width="97" height="81"/><rect class="tile-face" width="97" height="81"/><circle class="tile-dot" cx="48" cy="0" r="31"/><text class="tile-label" x="48" y="56">CAD<tspan x="48" dy="18">Drawings</tspan></text></g>
  <g class="tile" transform="translate(1242,657)"><rect class="tile-shadow" x="8" y="8" width="97" height="81"/><rect class="tile-face" width="97" height="81"/><circle class="tile-dot" cx="48" cy="0" r="31"/><text class="tile-label" x="48" y="56">Spec<tspan x="48" dy="18">Tools</tspan></text></g>
  <g class="tile" transform="translate(1351,657)"><rect class="tile-shadow" x="8" y="8" width="97" height="81"/><rect class="tile-face" width="97" height="81"/><circle class="tile-dot" cx="48" cy="0" r="31"/><text class="tile-label" x="48" y="56">Product<tspan x="48" dy="18">Selector</tspan></text></g>
  <g class="tile" transform="translate(1460,657)"><rect class="tile-shadow" x="8" y="8" width="97" height="81"/><rect class="tile-face" width="97" height="81"/><circle class="tile-dot" cx="48" cy="0" r="31"/><text class="tile-label" x="48" y="55">Product<tspan x="48" dy="18">Comparision</tspan></text></g>
  <g class="tile" transform="translate(1568,657)"><rect class="tile-shadow" x="8" y="8" width="97" height="81"/><rect class="tile-face" width="97" height="81"/><circle class="tile-dot" cx="48" cy="0" r="31"/><text class="tile-label" x="48" y="54">Design<tspan x="48" dy="18">Consideration</tspan></text></g>

  <g class="tile" transform="translate(1022,787)"><rect class="tile-shadow" x="8" y="8" width="97" height="81"/><rect class="tile-face" width="97" height="81"/><circle class="tile-dot" cx="48" cy="0" r="31"/><text class="tile-label" x="46" y="54">Color<tspan x="46" dy="18">Flexibility</tspan></text></g>
  <g class="tile" transform="translate(1132,787)"><rect class="tile-shadow" x="8" y="8" width="97" height="81"/><rect class="tile-face" width="97" height="81"/><circle class="tile-dot" cx="48" cy="0" r="31"/><text class="tile-label" x="46" y="57">Caculator</text></g>
  <g class="tile" transform="translate(1242,787)"><rect class="tile-shadow" x="8" y="8" width="97" height="81"/><rect class="tile-face" width="97" height="81"/><circle class="tile-dot" cx="48" cy="0" r="31"/><text class="tile-label" x="48" y="57">Performance<tspan x="48" dy="18">Data</tspan></text></g>
  <g class="tile" transform="translate(1351,787)"><rect class="tile-shadow" x="8" y="8" width="97" height="81"/><rect class="tile-face" width="97" height="81"/><circle class="tile-dot" cx="48" cy="0" r="31"/><text class="tile-label" x="48" y="57">Product Certs<tspan x="48" dy="18">(KTA, EQ, etc)</tspan></text></g>
  <g class="tile" transform="translate(1460,787)"><rect class="tile-shadow" x="8" y="8" width="97" height="81"/><rect class="tile-face" width="97" height="81"/><circle class="tile-dot" cx="48" cy="0" r="31"/><text class="tile-label" x="46" y="56">Building<tspan x="46" dy="18">Regulations</tspan></text></g>
  <g class="tile" transform="translate(1568,787)"><rect class="tile-shadow" x="8" y="8" width="97" height="81"/><rect class="tile-face" width="97" height="81"/><circle class="tile-dot" cx="48" cy="0" r="31"/><text class="tile-label" x="44" y="54">Technical<tspan x="44" dy="18">Data</tspan></text></g>

  <!-- engage panel -->
  <rect class="panel" x="1005" y="930" width="680" height="395" rx="24"/>
  <g class="tile" transform="translate(1027,982)"><rect class="tile-shadow" x="8" y="8" width="116" height="80"/><rect class="tile-face" width="116" height="80"/><circle class="tile-dot" cx="58" cy="-6" r="31"/><text class="tile-label" x="58" y="54">Testimonial</text></g>
  <g class="tile" transform="translate(1157,982)"><rect class="tile-shadow" x="8" y="8" width="116" height="80"/><rect class="tile-face" width="116" height="80"/><circle class="tile-dot" cx="58" cy="-6" r="31"/><text class="tile-label" x="58" y="56">Case Study</text></g>
  <g class="tile" transform="translate(1287,982)"><rect class="tile-shadow" x="8" y="8" width="116" height="80"/><rect class="tile-face" width="116" height="80"/><circle class="tile-dot" cx="58" cy="-6" r="31"/><text class="tile-label" x="58" y="54">White Paper</text></g>
  <g class="tile" transform="translate(1417,982)"><rect class="tile-shadow" x="8" y="8" width="116" height="80"/><rect class="tile-face" width="116" height="80"/><circle class="tile-dot" cx="58" cy="-6" r="31"/><text class="tile-label" x="58" y="56">Lead<tspan x="58" dy="18">Nuturing</tspan></text></g>
  <g class="tile" transform="translate(1547,982)"><rect class="tile-shadow" x="8" y="8" width="116" height="80"/><rect class="tile-face" width="116" height="80"/><circle class="tile-dot" cx="58" cy="-6" r="31"/><text class="tile-label" x="58" y="54">Members<tspan x="58" dy="18">Area</tspan></text></g>

  <g class="tile" transform="translate(1027,1100)"><rect class="tile-shadow" x="8" y="8" width="116" height="83"/><rect class="tile-face" width="116" height="83"/><circle class="tile-dot" cx="58" cy="-2" r="31"/><text class="tile-label" x="58" y="55">Social<tspan x="58" dy="18">Medias</tspan></text></g>
  <g class="tile" transform="translate(1157,1100)"><rect class="tile-shadow" x="8" y="8" width="116" height="83"/><rect class="tile-face" width="116" height="83"/><circle class="tile-dot" cx="58" cy="-2" r="31"/><text class="tile-label" x="58" y="57">Lead Automation<tspan x="58" dy="18">(Nurturely)</tspan></text></g>
  <g class="tile" transform="translate(1287,1100)"><rect class="tile-shadow" x="8" y="8" width="116" height="83"/><rect class="tile-face" width="116" height="83"/><circle class="tile-dot" cx="58" cy="-2" r="31"/><text class="tile-label" x="58" y="55">Email</text></g>
  <g class="tile" transform="translate(1417,1100)"><rect class="tile-shadow" x="8" y="8" width="116" height="83"/><rect class="tile-face" width="116" height="83"/><circle class="tile-dot" cx="58" cy="-2" r="31"/><text class="tile-label" x="58" y="57">Event - Road<tspan x="58" dy="18">Shows</tspan></text></g>
  <g class="tile" transform="translate(1547,1100)"><rect class="tile-shadow" x="8" y="8" width="116" height="83"/><rect class="tile-face" width="116" height="83"/><circle class="tile-dot" cx="58" cy="-2" r="31"/><text class="tile-label" x="58" y="55">Ebooks</text></g>

  <g class="tile" transform="translate(1027,1222)"><rect class="tile-shadow" x="8" y="8" width="116" height="83"/><rect class="tile-face" width="116" height="83"/><circle class="tile-dot" cx="58" cy="-4" r="31"/><text class="tile-label" x="58" y="57">Video<tspan x="58" dy="18">Case Studies</tspan></text></g>
  <g class="tile" transform="translate(1157,1222)"><rect class="tile-shadow" x="8" y="8" width="116" height="83"/><rect class="tile-face" width="116" height="83"/><circle class="tile-dot" cx="58" cy="-4" r="31"/><text class="tile-label" x="58" y="59">Remarketing</text></g>
  <g class="tile" transform="translate(1287,1222)"><rect class="tile-shadow" x="8" y="8" width="116" height="83"/><rect class="tile-face" width="116" height="83"/><circle class="tile-dot" cx="58" cy="-4" r="31"/><text class="tile-label" x="58" y="57">Product<tspan x="58" dy="18">Launches</tspan></text></g>
  <g class="tile" transform="translate(1417,1222)"><rect class="tile-shadow" x="8" y="8" width="116" height="83"/><rect class="tile-face" width="116" height="83"/><circle class="tile-dot" cx="58" cy="-4" r="31"/><text class="tile-label" x="58" y="59">Data Sheets</text></g>
  <g class="tile" transform="translate(1547,1222)"><rect class="tile-shadow" x="8" y="8" width="116" height="83"/><rect class="tile-face" width="116" height="83"/><circle class="tile-dot" cx="58" cy="-4" r="31"/><text class="tile-label" x="58" y="57">Online<tspan x="58" dy="18">Tools</tspan></text></g>

  <!-- supply chain panel -->
  <rect class="panel" x="1762" y="247" width="675" height="1068" rx="28"/>

  <!-- regulators panel (behind the project cards) -->
  <rect x="2172" y="718" width="283" height="382" rx="18" fill="var(--paper)" stroke="var(--ink)" stroke-width="4"/>
  <g class="roles">
    <rect class="tile-shadow" x="2196" y="736" width="125" height="42"/><rect class="role-tag" x="2190" y="730" width="125" height="42"/><text class="role-text" x="2252" y="746">Structure<tspan x="2252" dy="17">Engineers</tspan></text>
    <rect class="tile-shadow" x="2329" y="736" width="122" height="42"/><rect class="role-tag" x="2323" y="730" width="122" height="42"/><text class="role-text" x="2385" y="746">M&amp;E<tspan x="2385" dy="17">Engineers</tspan></text>
    <rect class="tile-shadow" x="2329" y="789" width="122" height="39"/><rect class="role-tag" x="2323" y="783" width="122" height="39"/><text class="role-text" x="2385" y="808">Architects</text>
    <rect class="tile-shadow" x="2329" y="841" width="122" height="40"/><rect class="role-tag" x="2323" y="835" width="122" height="40"/><text class="role-text" x="2385" y="860">Specifiers</text>
    <rect class="tile-shadow" x="2329" y="894" width="122" height="40"/><rect class="role-tag" x="2323" y="888" width="122" height="40"/><text class="role-text" x="2385" y="903">Quantity<tspan x="2385" dy="17">Surveyors</tspan></text>
    <rect class="tile-shadow" x="2329" y="948" width="122" height="40"/><rect class="role-tag" x="2323" y="942" width="122" height="40"/><text class="role-text" x="2385" y="957">Health &amp; Safety<tspan x="2385" dy="17">(HSE)</tspan></text>
    <rect class="tile-shadow" x="2329" y="1001" width="122" height="42"/><rect class="role-tag" x="2323" y="995" width="122" height="42"/><text class="role-text" x="2385" y="1011">Building Control<tspan x="2385" dy="17">Officer</tspan></text>
    <rect class="tile-shadow" x="2196" y="1056" width="125" height="40"/><rect class="role-tag" x="2190" y="1050" width="125" height="40"/><text class="role-text" x="2252" y="1065">Environment<tspan x="2252" dy="17">Officer</tspan></text>
    <rect class="tile-shadow" x="2329" y="1056" width="122" height="40"/><rect class="role-tag" x="2323" y="1050" width="122" height="40"/><text class="role-text" x="2385" y="1065">Planning<tspan x="2385" dy="17">Officer</tspan></text>
  </g>

  <!-- connectors -->
  <path class="flow-ink" d="M1815 1255 V455 H1945"/>
  <path class="arrow" d="M1790 1275 L1815 1240 L1840 1275 Z"/>
  <path class="flow-ink" d="M1905 325 H1920 V430 H1935"/>
  <path class="arrow" d="M1932 418 L1952 430 L1932 442 Z"/>
  <path class="flow-ink" d="M2180 310 H2165 V430 H2155"/>
  <path class="arrow" d="M2158 418 L2138 430 L2158 442 Z"/>
  <path class="flow-ink" d="M1945 518 H1893 V545 M2150 518 H2202 V545 M2047 553 V595"/>
  <path class="arrow" d="M1881 538 L1893 556 L1905 538 Z M2190 538 L2202 556 L2214 538 Z M2035 590 L2047 608 L2059 590 Z"/>
  <path class="flow-ink" d="M1950 588 H1972 V640 H1995 M2145 588 H2122 V640 H2100"/>
  <path class="arrow" d="M1990 628 L2008 640 L1990 652 Z M2105 628 L2087 640 L2105 652 Z"/>
  <path class="flow-ink" d="M2047 800 V850"/>
  <path class="arrow" d="M2035 805 L2047 785 L2059 805 Z M2035 845 L2047 865 L2059 845 Z"/>
  <path class="flow-ink" d="M1955 865 H1985 V902 H1995 M2135 865 H2105 V902 H2095"/>
  <path class="arrow" d="M1990 890 L2008 902 L1990 914 Z M2100 890 L2082 902 L2100 914 Z"/>
  <path class="flow-ink" d="M2047 1018 V1080"/>
  <path class="arrow" d="M2022 1065 L2047 1105 L2072 1065 Z"/>
  <path class="flow-ink" d="M2047 1100 V1145 M2135 1205 H2210"/>

  <!-- factory -->
  <circle cx="2047" cy="410" r="96" fill="var(--ink)"/>
  <circle cx="2047" cy="410" r="86" fill="#ffffff" role="img" aria-label="Factory with smoking chimney illustration"/>
  <rect x="1940" y="480" width="215" height="72" rx="24" fill="var(--ink)"/>
  <rect x="1947" y="487" width="201" height="58" rx="19" fill="var(--paper)"/>
  <text class="badge-text" x="2048" y="513" font-size="19" textLength="100" lengthAdjust="spacingAndGlyphs">PRODUCT</text>
  <text class="badge-text" x="2048" y="538" font-size="19" textLength="176" lengthAdjust="spacingAndGlyphs">MANUFACTURER</text>

  <!-- supply tiles -->
  <g class="tile" transform="translate(1810,322)"><rect class="tile-shadow" x="8" y="8" width="95" height="83"/><rect class="tile-face" width="95" height="83"/><circle class="tile-dot" cx="47" cy="-14" r="37"/><text class="tile-label" x="47" y="60">Raw<tspan x="47" dy="18">Materials</tspan></text></g>
  <g class="tile" transform="translate(2180,322)"><rect class="tile-shadow" x="8" y="8" width="100" height="83"/><rect class="tile-face" width="100" height="83"/><circle class="tile-dot" cx="50" cy="-12" r="37"/><text class="tile-label" x="50" y="60">Imported<tspan x="50" dy="18">Products</tspan></text></g>
  <g class="tile" transform="translate(1838,607)"><rect class="tile-shadow" x="8" y="8" width="112" height="138"/><rect class="tile-face" width="112" height="138"/><circle class="tile-dot" cx="55" cy="-15" r="37"/><text class="tile-label" x="56" y="46">Multi-<tspan x="56" dy="18">manufacturers</tspan><tspan x="56" dy="18">within a</tspan><tspan x="56" dy="18">building</tspan><tspan x="56" dy="18">system</tspan></text></g>
  <g class="tile" transform="translate(1990,660)"><rect class="tile-shadow" x="8" y="8" width="115" height="125"/><rect class="tile-face" width="115" height="125"/><circle class="tile-dot" cx="57" cy="-20" r="37"/><text class="tile-label" x="58" y="45">Sub-contractor<tspan x="58" dy="18">or</tspan><tspan x="58" dy="18">Specialist</tspan><tspan x="58" dy="18">Contractor</tspan></text></g>
  <g class="tile" transform="translate(2145,607)"><rect class="tile-shadow" x="8" y="8" width="113" height="98"/><rect class="tile-face" width="113" height="98"/><circle class="tile-dot" cx="57" cy="-14" r="37"/><text class="tile-label" x="57" y="64">Manufacturer<tspan x="57" dy="18">Installer</tspan></text></g>
  <g class="tile" transform="translate(1867,880)"><rect class="tile-shadow" x="8" y="8" width="101" height="138"/><rect class="tile-face" width="101" height="138"/><circle class="tile-dot" cx="49" cy="-15" r="37"/><text class="tile-label" x="50" y="107">Finance</text></g>
  <g class="tile" transform="translate(1995,920)"><rect class="tile-shadow" x="8" y="8" width="100" height="98"/><rect class="tile-face" width="100" height="98"/><circle class="tile-dot" cx="49" cy="-18" r="37"/><text class="tile-label" x="50" y="65">Main<tspan x="50" dy="18">Contractor</tspan></text></g>
  <g class="tile" transform="translate(2122,880)"><rect class="tile-shadow" x="8" y="8" width="100" height="145"/><rect class="tile-face" width="100" height="145"/><circle class="tile-dot" cx="49" cy="-14" r="37"/><text class="tile-label" x="50" y="99">Project<tspan x="50" dy="18">Manager</tspan></text></g>

  <!-- work & end user -->
  <rect x="1955" y="1143" width="180" height="117" rx="26" fill="var(--ink)"/>
  <rect x="1963" y="1151" width="164" height="101" rx="20" fill="var(--paper)"/>
  <text class="badge-text" x="2045" y="1200" textLength="98" lengthAdjust="spacingAndGlyphs">WORK IS</text>
  <text class="badge-text" x="2045" y="1227" textLength="148" lengthAdjust="spacingAndGlyphs">CARRIED OUT</text>
  <circle cx="2282" cy="1198" r="80" fill="var(--ink)"/>
  <circle cx="2282" cy="1198" r="70" fill="#ffffff" role="img" aria-label="Family of end users illustration"/>
  <rect x="2200" y="1253" width="162" height="55" rx="26" fill="var(--ink)"/>
  <rect x="2206" y="1259" width="150" height="43" rx="21" fill="var(--paper)"/>
  <text class="badge-text" x="2281" y="1288" textLength="110" lengthAdjust="spacingAndGlyphs">END USER</text>
</svg>
</body>
</html>
```